Business card n Letter heads for an IT Company
Quorvane Systems JLT
Business card n Letter heads for an IT Company - Information Technology
Creative Brief
Bright & Fun-filled
Rohan Mextapur
Sales Manager
2817,Halvering Business Tower, Pelmar D, Dubai UAE
rohan@quorvane.com
www.quorvane.com
An Dravolk Group Company

```html
<!DOCTYPE html>
<html lang="en">
<head>
<meta charset="utf-8">
<title>Quorvane Systems JLT – Stationery</title>
<link href="https://fonts.googleapis.com/css2?family=Ubuntu:wght@400;500&display=swap" rel="stylesheet">
<style>
:root{
  --bg:#ebebeb;
  --paper:#ffffff;
  --brand-red:#d3161d;
  --brand-red-soft:rgba(211,22,29,.12);
  --ink:#6a6a6a;
  --ink-light:#9a9a9a;
}
*{box-sizing:border-box;margin:0;padding:0}
html,body{width:1200px;height:936px;overflow:hidden;background:var(--bg);font-family:"Ubuntu",Arial,sans-serif}
.stage{position:relative;width:1200px;height:936px}
.sheet{position:absolute;background:var(--paper)}
.brand{display:flex;align-items:center;gap:6px;color:var(--brand-red);font-weight:500;line-height:1}
.brand-square{display:inline-block;background:var(--brand-red)}
.contact-lines{color:var(--ink);font-size:6px;line-height:9px}
.contact-lines p::before{content:"";display:inline-block;width:4px;height:4px;margin-right:4px;background:var(--brand-red);vertical-align:middle}

.letterhead{left:178px;top:51px;width:279px;height:596px}
.letterhead .bar{position:absolute;left:0;top:34px;width:4px;height:36px;background:var(--brand-red)}
.letterhead .brand{position:absolute;left:12px;top:42px;font-size:18px}
.letterhead .brand-square{width:10px;height:10px}
.letterhead .contact-lines{position:absolute;right:18px;top:40px;font-size:5px;line-height:7px}
.letterhead .watermark{position:absolute;left:112px;top:268px;width:56px;height:56px;background:var(--brand-red-soft)}

.folder{left:497px;top:46px;width:518px;height:609px}
.folder .brand{position:absolute;left:0;right:0;top:372px;justify-content:center;font-size:52px;gap:12px}
.folder .brand-square{width:26px;height:26px}

.card-front{left:36px;top:655px;width:208px;height:81px}
.card-front .brand{position:absolute;left:10px;top:10px;font-size:16px;gap:4px}
.card-front .brand-square{width:8px;height:8px}
.card-front .contact-lines{position:absolute;left:10px;top:36px;font-size:5px;line-height:7px}
.card-front .person{position:absolute;right:10px;top:52px;text-align:right;color:var(--ink);font-size:6px;line-height:8px}
.card-front .person strong{color:var(--brand-red);font-weight:500}

.card-back{left:36px;top:746px;width:208px;height:91px;background:var(--brand-red)}
.card-back .brand{position:absolute;left:0;right:0;top:28px;justify-content:center;color:#fff;font-size:20px}
.card-back .brand-square{width:10px;height:10px;background:#fff}
.card-back .web{position:absolute;left:12px;bottom:8px;color:#fff;font-size:5px;letter-spacing:.5px}

.envelope-front{left:264px;top:665px;width:421px;height:198px}
.envelope-front .brand{position:absolute;left:14px;top:18px;font-size:20px}
.envelope-front .brand-square{width:10px;height:10px}
.envelope-front .address{position:absolute;left:14px;top:46px;color:var(--ink);font-size:6px}

.envelope-back{left:736px;top:665px;width:431px;height:198px}
.envelope-back svg{position:absolute;inset:0}
.envelope-back .web{position:absolute;left:0;right:0;top:38px;text-align:center;color:#fff;font-size:8px;letter-spacing:4px}
</style>
</head>
<body>
<main class="stage">

  <section class="sheet letterhead" aria-label="Letterhead">
    <span class="bar"></span>
    <div class="brand"><span class="brand-square"></span>quorvane</div>
    <div class="contact-lines">
      <p>2817,Halvering Business Tower</p>
      <p>Pelmar D, Dubai UAE</p>
      <p>T +971 4 555 0142</p>
      <p>rohan@quorvane.com</p>
      <p>www.quorvane.com</p>
    </div>
    <span class="watermark"></span>
  </section>

  <section class="sheet folder" aria-label="Presentation folder">
    <div class="brand"><span class="brand-square"></span>quorvane</div>
  </section>

  <section class="sheet card-front" aria-label="Business card front">
    <div class="brand"><span class="brand-square"></span>quorvane</div>
    <div class="contact-lines">
      <p>2817,Halvering Business Tower</p>
      <p>Pelmar D, Dubai UAE</p>
      <p>rohan@quorvane.com</p>
      <p>www.quorvane.com</p>
    </div>
    <div class="person"><strong>Rohan Mextapur</strong><br>Sales Manager</div>
  </section>

  <section class="sheet card-back" aria-label="Business card back">
    <div class="brand"><span class="brand-square"></span>quorvane</div>
    <p class="web">www.quorvane.com</p>
  </section>

  <section class="sheet envelope-front" aria-label="Envelope front">
    <div class="brand"><span class="brand-square"></span>quorvane</div>
    <p class="address">2817,Halvering Business Tower, Pelmar D, Dubai UAE</p>
  </section>

  <section class="sheet envelope-back" aria-label="Envelope back">
    <svg width="431" height="198" viewBox="0 0 431 198">
      <rect width="431" height="198" fill="var(--paper)"/>
      <polygon points="0,0 431,0 431,62 215,112 0,62" fill="var(--brand-red)"/>
    </svg>
    <p class="web">WWW.QUORVANE.COM</p>
  </section>

</main>
</body>
</html>
```